New Innovative Counselling and psychotherapy Service needs Business Card design

Keep it simple and professional. On one side, just company name and logo (perhaps in all blue) and maybe a tag line.

On other side (all white) my name and Qualifications in centre

Industry/Entity Type

Health And Wellness

Contact Information for Business Card

Derek Hollis
Counsellor & Psychotherapist
BSc (Psychol.), BA, Dip. (Couns. & Psych.), PG.Cert (CBT), MGVrA, NWTF

I will also require Mobile no, Email and web site address of which I'll pass on to final designer.

Font styles to use
Sans Serif

Requirements
Must have
• My Logo Only and please use the colours in logo that is in it.
Should not have
• Any other images

```html
<!DOCTYPE html>
<html lang="en">
<head>
<meta charset="utf-8">
<title>Harbor Lane – Business Card</title>
<link href="https://fonts.googleapis.com/css2?family=Roboto:wght@400;500&display=swap" rel="stylesheet">
<style>
  :root {
    --page-bg: #ecedef;
    --card-white: #ffffff;
    --pattern-tint-a: #f7fbfd;
    --pattern-tint-b: #e6f4fa;
    --brand-blue: #1ea6dc;
    --brand-blue-light: #3fc0e8;
    --brand-blue-deep: #139bd3;
    --brand-green: #6cc04a;
    --ink-dark: #2e3338;
    --ink-light: #ffffff;
    --card-shadow: rgba(20, 40, 60, 0.18);
  }
  * { margin: 0; padding: 0; box-sizing: border-box; }
  html, body {
    width: 1200px;
    height: 805px;
    overflow: hidden;
    background: var(--page-bg);
    font-family: "Roboto", Arial, sans-serif;
  }
  .canvas {
    width: 1200px;
    height: 805px;
    display: flex;
    align-items: center;
    justify-content: center;
    gap: 50px;
  }
  .card {
    width: 520px;
    height: 297px;
    border-radius: 22px;
    overflow: hidden;
    position: relative;
    box-shadow: 0 10px 28px var(--card-shadow);
  }

  /* Front */
  .card--front { background: var(--card-white); }
  .front-backdrop {
    position: absolute;
    inset: 0;
    background: radial-gradient(circle at 50% 50%, var(--pattern-tint-a) 0%, var(--pattern-tint-b) 100%);
  }
  .front-brand {
    position: absolute;
    left: 50%;
    top: 50%;
    transform: translate(-50%, -50%);
    display: flex;
    align-items: center;
    gap: 16px;
  }
  .brand-dot {
    width: 96px;
    height: 96px;
    border-radius: 50%;
    background: var(--brand-blue);
    flex: none;
  }
  .brand-name {
    font-weight: 400;
    color: var(--ink-dark);
    white-space: nowrap;
  }
  .front-brand .brand-name { font-size: 34px; }

  /* Back */
  .card--back {
    background: linear-gradient(160deg, var(--brand-blue-light) 0%, var(--brand-blue) 55%, var(--brand-blue-deep) 100%);
    color: var(--ink-light);
  }
  .back-brand {
    position: absolute;
    left: 34px;
    top: 128px;
    display: flex;
    align-items: center;
    gap: 8px;
  }
  .back-brand .brand-dot { width: 28px; height: 28px; background: var(--ink-light); }
  .back-brand .brand-name { font-size: 19px; }
  .divider {
    position: absolute;
    left: 222px;
    top: 74px;
    width: 2px;
    height: 152px;
    background: var(--ink-light);
  }
  .details {
    position: absolute;
    left: 238px;
    top: 72px;
    right: 20px;
  }
  .person-name {
    color: var(--brand-green);
    font-size: 27px;
    font-weight: 500;
    line-height: 1.1;
  }
  .person-role {
    font-size: 16px;
    font-weight: 400;
    margin-top: 4px;
  }
  .person-quals {
    font-size: 10.5px;
    line-height: 1.35;
    margin-top: 3px;
  }
  .contacts {
    list-style: none;
    margin-top: 12px;
    font-size: 11px;
  }
  .contacts li {
    display: flex;
    align-items: center;
    gap: 9px;
    height: 22px;
  }
  .contact-icon { width: 15px; height: 15px; flex: none; }
</style>
</head>
<body>
<main class="canvas">
  <section class="card card--front" aria-label="Business card front">
    <div class="front-backdrop" role="img" aria-label="Faint repeating brand pattern in light blue and green"></div>
    <div class="front-brand">
      <span class="brand-dot"></span>
      <span class="brand-name">Harbor Lane</span>
    </div>
  </section>

  <section class="card card--back" aria-label="Business card back">
    <div class="back-brand">
      <span class="brand-dot"></span>
      <span class="brand-name">Harbor Lane</span>
    </div>
    <div class="divider"></div>
    <div class="details">
      <h1 class="person-name">Derek Hollis</h1>
      <p class="person-role">Counsellor &amp; Psychotherapist</p>
      <p class="person-quals">BSc (Psychol.), BA, Dip. (Couns. &amp; Psych.),<br>PG.Cert (CBT), MGVrA, NWTF</p>
      <ul class="contacts">
        <li>
          <svg class="contact-icon" viewBox="0 0 16 16" aria-hidden="true">
            <rect x="4" y="1" width="8" height="14" rx="1.5" fill="none" stroke="var(--brand-green)" stroke-width="1.6"/>
            <circle cx="8" cy="12.5" r="0.9" fill="var(--brand-green)"/>
          </svg>
          <span>0000 000 000</span>
        </li>
        <li>
          <svg class="contact-icon" viewBox="0 0 16 16" aria-hidden="true">
            <circle cx="8" cy="8" r="7.5" fill="var(--brand-green)"/>
            <rect x="4" y="5" width="8" height="6" fill="none" stroke="var(--ink-light)" stroke-width="1"/>
            <path d="M4 5 L8 8.5 L12 5" fill="none" stroke="var(--ink-light)" stroke-width="1"/>
          </svg>
          <span>youremailaddress@mailbox.com</span>
        </li>
        <li>
          <svg class="contact-icon" viewBox="0 0 16 16" aria-hidden="true">
            <circle cx="8" cy="8" r="7.5" fill="var(--brand-green)"/>
            <circle cx="8" cy="8" r="4.5" fill="none" stroke="var(--ink-light)" stroke-width="1"/>
            <ellipse cx="8" cy="8" rx="2" ry="4.5" fill="none" stroke="var(--ink-light)" stroke-width="1"/>
            <line x1="3.5" y1="8" x2="12.5" y2="8" stroke="var(--ink-light)" stroke-width="1"/>
          </svg>
          <span>www.yourwebsite.com</span>
        </li>
      </ul>
    </div>
  </section>
</main>
</body>
</html>
```